Showroom Quote Web Application - Material Design wanted

This web app is an internal application that will be used by one of our customers to build quotes and produce orders of retail items with their customers

the overall design should use the colour pallet provided and have a clean and simple interface

we'd like to go with a material design type of look

attached mockups are just a rough stab at some layouts to give you an example, please feel free to reach out with any questions.

Please don't get hung up on the specific pages, they were intended to provide context, we are looking for a high level design using the provided colour schemes and fonts, additional work may follow for the selected designer when it comes to specific pages or work flows.

Sorry for the short timeline, we have a tight deadline on this one.

Target Market(s)

internal application for customer

Industry/Entity Type

Retail

Other font styles liked:
• see attached doc for fonts

Requirements
Must have
• simple and clean interface
• intuitive design
Nice to have
• see attached documents for logo colour schemes and fonts
• these must be incorporated into the design

```html
<!DOCTYPE html>
<html lang="en">
<head>
<meta charset="utf-8">
<title>Plumbing Showroom Quote System – Completed Quotes</title>
<link rel="stylesheet" href="https://fonts.googleapis.com/css2?family=Hind:wght@400;500;600&display=swap">
<style>
  :root {
    --gold: #b8914a;
    --navy: #0d3a7a;
    --ink: #1f1f1f;
    --muted: #4a4a4a;
    --sidebar-bg: #f0f0f0;
    --stripe: #f5f5f5;
    --search-bg: #efefef;
    --line: #d6d6d6;
    --page: #ffffff;
  }
  * { box-sizing: border-box; margin: 0; padding: 0; }
  html, body { width: 1200px; height: 800px; overflow: hidden; background: var(--page); }
  body { font-family: "Hind", sans-serif; color: var(--ink); position: relative; }

  .sidebar { position: absolute; left: 0; top: 0; width: 224px; height: 800px; background: var(--sidebar-bg); }
  .brand { position: absolute; top: 38px; left: 0; width: 224px; text-align: center; }
  .brand-mark { width: 48px; height: 48px; background: var(--gold); border-radius: 4px; margin: 0 auto 14px; }
  .brand-name { font-size: 13px; font-weight: 600; color: var(--muted); line-height: 15px; letter-spacing: .2px; }
  .divider { position: absolute; top: 203px; left: 22px; width: 180px; height: 1px; background: var(--line); }
  .new-quote { position: absolute; top: 226px; left: 22px; width: 180px; height: 33px; border-radius: 17px; background: var(--navy); color: #fff; font-size: 15.5px; font-weight: 600; display: flex; align-items: center; padding-left: 9px; padding-top: 2px; }
  .new-quote svg { margin-right: 24px; margin-top: -2px; }
  .nav-item { position: absolute; left: 0; width: 224px; height: 36px; display: flex; align-items: center; padding-left: 22px; font-size: 15.5px; font-weight: 500; color: var(--ink); }
  .nav-item svg { width: 30px; height: 28px; margin-right: 21px; flex-shrink: 0; }
  .nav-item.active { color: var(--gold); font-weight: 600; }
  .nav-item.active::before { content: ""; position: absolute; left: 0; top: 2px; width: 2px; height: 32px; background: var(--gold); }

  .tabs { position: absolute; top: 24px; left: 262px; }
  .tab { font-size: 22px; font-weight: 500; color: var(--ink); position: absolute; white-space: nowrap; }
  .tab.current { color: var(--gold); font-weight: 600; }
  .tab.current::after { content: ""; position: absolute; left: 0; right: 0; top: 34px; height: 3px; background: var(--gold); }
  .search { position: absolute; top: 23px; left: 743px; width: 435px; height: 37px; border-radius: 19px; background: var(--search-bg); display: flex; align-items: center; padding-left: 14px; padding-top: 2px; font-size: 15px; font-weight: 500; color: var(--muted); }
  .search svg { margin-right: 18px; margin-top: -2px; flex-shrink: 0; }

  .quote-table { position: absolute; left: 276px; top: 0; width: 872px; }
  .row { position: absolute; left: 0; width: 872px; height: 53px; font-size: 15.5px; font-weight: 500; }
  .row.striped { background: var(--stripe); }
  .row.head { top: 84px; height: 40px; border-bottom: 1px solid var(--line); }
  .cell { position: absolute; top: 50%; transform: translateY(-44%); white-space: nowrap; line-height: 1; }
  .c-quote { left: 33px; }
  .c-customer { left: 150px; font-weight: 600; }
  .c-date { left: 379px; transform: translate(-50%, -44%); }
  .c-value { left: 509px; transform: translate(-50%, -44%); color: var(--navy); font-weight: 600; }
  .c-desc { left: 629px; }
  .c-edit { left: 832px; transform: translateY(-50%); width: 17px; height: 17px; }
  .c-edit svg { display: block; }
  .row.head .c-customer, .row.head .c-value { font-weight: 500; color: var(--ink); }
  .row.head .c-edit { left: 824px; width: auto; height: auto; transform: translateY(-44%); }

  .fab { position: absolute; left: 1117px; top: 707px; width: 60px; height: 60px; border-radius: 50%; background: var(--navy); box-shadow: 0 3px 8px rgba(0,0,0,.3); display: flex; align-items: center; justify-content: center; }
</style>
</head>
<body>
  <aside class="sidebar">
    <div class="brand">
      <div class="brand-mark"></div>
      <div class="brand-name">PLUMBING SHOWROOM<br>QUOTE SYSTEM</div>
    </div>
    <div class="divider"></div>
    <div class="new-quote">
      <svg width="16" height="16" viewBox="0 0 16 16"><circle cx="8" cy="8" r="8" fill="#fff"/><path d="M8 4v8M4 8h8" stroke="#0d3a7a" stroke-width="2"/></svg>
      New Quote
    </div>
    <div class="nav-item active" style="top:284px">
      <svg viewBox="0 0 30 28"><rect x="1" y="1" width="28" height="26" rx="2" fill="none" stroke="#b8914a" stroke-width="2"/><path d="M6 9h18M6 14h18M6 19h18" stroke="#b8914a" stroke-width="2"/></svg>
      Dashboard
    </div>
    <div class="nav-item" style="top:344px">
      <svg viewBox="0 0 30 28"><path d="M1 4h24" stroke="#4a4a4a" stroke-width="2"/><rect x="4" y="7" width="25" height="20" fill="#4a4a4a"/><circle cx="16.5" cy="14" r="3" fill="#f0f0f0"/><path d="M11 23c0-4 3-5 5.5-5s5.5 1 5.5 5z" fill="#f0f0f0"/></svg>
      Customers
    </div>
    <div class="nav-item" style="top:402px">
      <svg viewBox="0 0 30 28"><circle cx="9" cy="8" r="5" fill="#4a4a4a"/><circle cx="21" cy="8" r="5" fill="#4a4a4a"/><path d="M0 26c0-8 4-11 9-11s9 3 9 11z" fill="#4a4a4a"/><path d="M12 26c0-8 4-11 9-11s9 3 9 11z" fill="#4a4a4a"/></svg>
      Staffs
    </div>
  </aside>

  <nav class="tabs">
    <span class="tab" style="left:0">Pending</span>
    <span class="tab current" style="left:105px">Completed</span>
    <span class="tab" style="left:236px">Errors</span>
  </nav>
  <div class="search">
    <svg width="18" height="18" viewBox="0 0 18 18"><circle cx="7.5" cy="7.5" r="5.5" fill="none" stroke="#1f1f1f" stroke-width="2"/><path d="M11.5 11.5l5 5" stroke="#1f1f1f" stroke-width="2"/></svg>
    Search quote number / customer
  </div>

  <section class="quote-table">
    <div class="row head">
      <span class="cell c-quote">QUOTE #</span>
      <span class="cell c-customer">CUSTOMERS</span>
      <span class="cell c-date">DATE</span>
      <span class="cell c-value">VALUE</span>
      <span class="cell c-desc">DESCRIPTION</span>
      <span class="cell c-edit">EDIT</span>
    </div>

    <div class="row" style="top:130px"><span class="cell c-quote">001728</span><span class="cell c-customer">Orrin Vaskett</span><span class="cell c-date">28 Oct 2017</span><span class="cell c-value">$4,200.00</span><span class="cell c-desc">New House</span><span class="cell c-edit"><svg width="17" height="17" viewBox="0 0 17 17"><path d="M8 2H2v13h13V9" fill="none" stroke="#b8914a" stroke-width="1.8"/><path d="M6 11l1-3 7-7 2 2-7 7z" fill="#b8914a"/></svg></span></div>
    <div class="row striped" style="top:183px"><span class="cell c-quote">002460</span><span class="cell c-customer">Tamsin Lyle Brevard</span><span class="cell c-date">16 Oct 2017</span><span class="cell c-value">$3,000.00</span><span class="cell c-desc">New Apartment</span><span class="cell c-edit"><svg width="17" height="17" viewBox="0 0 17 17"><path d="M8 2H2v13h13V9" fill="none" stroke="#b8914a" stroke-width="1.8"/><path d="M6 11l1-3 7-7 2 2-7 7z" fill="#b8914a"/></svg></span></div>
    <div class="row" style="top:236px"><span class="cell c-quote">001039</span><span class="cell c-customer">Dorian Pellish</span><span class="cell c-date">7 Oct 2017</span><span class="cell c-value">$5,100.00</span><span class="cell c-desc">Old House</span><span class="cell c-edit"><svg width="17" height="17" viewBox="0 0 17 17"><path d="M8 2H2v13h13V9" fill="none" stroke="#b8914a" stroke-width="1.8"/><path d="M6 11l1-3 7-7 2 2-7 7z" fill="#b8914a"/></svg></span></div>
    <div class="row striped" style="top:289px"><span class="cell c-quote">010580</span><span class="cell c-customer">Lorna Quibbet</span><span class="cell c-date">30 Sep 2017</span><span class="cell c-value">$1,200.00</span><span class="cell c-desc">New Condo Unit</span><span class="cell c-edit"><svg width="17" height="17" viewBox="0 0 17 17"><path d="M8 2H2v13h13V9" fill="none" stroke="#b8914a" stroke-width="1.8"/><path d="M6 11l1-3 7-7 2 2-7 7z" fill="#b8914a"/></svg></span></div>
    <div class="row" style="top:342px"><span class="cell c-quote">002840</span><span class="cell c-customer">Marten Oswick</span><span class="cell c-date">22 Sep 2017</span><span class="cell c-value">$2,600.00</span><span class="cell c-desc">Old Apartment</span><span class="cell c-edit"><svg width="17" height="17" viewBox="0 0 17 17"><path d="M8 2H2v13h13V9" fill="none" stroke="#b8914a" stroke-width="1.8"/><path d="M6 11l1-3 7-7 2 2-7 7z" fill="#b8914a"/></svg></span></div>
    <div class="row striped" style="top:395px"><span class="cell c-quote">000984</span><span class="cell c-customer">Crispin Arnhollow</span><span class="cell c-date">14 Sep 2017</span><span class="cell c-value">$4,100.00</span><span class="cell c-desc">New House</span><span class="cell c-edit"><svg width="17" height="17" viewBox="0 0 17 17"><path d="M8 2H2v13h13V9" fill="none" stroke="#b8914a" stroke-width="1.8"/><path d="M6 11l1-3 7-7 2 2-7 7z" fill="#b8914a"/></svg></span></div>
    <div class="row" style="top:448px"><span class="cell c-quote">002023</span><span class="cell c-customer">Callum Drevitt</span><span class="cell c-date">2 Sep 2017</span><span class="cell c-value">$5,000.00</span><span class="cell c-desc">New Condo Unit</span><span class="cell c-edit"><svg width="17" height="17" viewBox="0 0 17 17"><path d="M8 2H2v13h13V9" fill="none" stroke="#b8914a" stroke-width="1.8"/><path d="M6 11l1-3 7-7 2 2-7 7z" fill="#b8914a"/></svg></span></div>
    <div class="row striped" style="top:501px"><span class="cell c-quote">000501</span><span class="cell c-customer">Bram Haskovel</span><span class="cell c-date">25 Aug 2017</span><span class="cell c-value">$3,200.00</span><span class="cell c-desc">Old House</span><span class="cell c-edit"><svg width="17" height="17" viewBox="0 0 17 17"><path d="M8 2H2v13h13V9" fill="none" stroke="#b8914a" stroke-width="1.8"/><path d="M6 11l1-3 7-7 2 2-7 7z" fill="#b8914a"/></svg></span></div>
    <div class="row" style="top:554px"><span class="cell c-quote">002584</span><span class="cell c-customer">Fiorella Benvasquez</span><span class="cell c-date">18 Aug 2017</span><span class="cell c-value">$1,500.00</span><span class="cell c-desc">New Apartment</span><span class="cell c-edit"><svg width="17" height="17" viewBox="0 0 17 17"><path d="M8 2H2v13h13V9" fill="none" stroke="#b8914a" stroke-width="1.8"/><path d="M6 11l1-3 7-7 2 2-7 7z" fill="#b8914a"/></svg></span></div>
    <div class="row striped" style="top:607px"><span class="cell c-quote">001023</span><span class="cell c-customer">Corwin Tamsley</span><span class="cell c-date">10 Aug 2017</span><span class="cell c-value">$4,300.00</span><span class="cell c-desc">Old Condo Unit</span><span class="cell c-edit"><svg width="17" height="17" viewBox="0 0 17 17"><path d="M8 2H2v13h13V9" fill="none" stroke="#b8914a" stroke-width="1.8"/><path d="M6 11l1-3 7-7 2 2-7 7z" fill="#b8914a"/></svg></span></div>
    <div class="row" style="top:660px"><span class="cell c-quote">002748</span><span class="cell c-customer">Jorah Canfeld</span><span class="cell c-date">28 Jul 2017</span><span class="cell c-value">$2,200.00</span><span class="cell c-desc">Old House</span><span class="cell c-edit"><svg width="17" height="17" viewBox="0 0 17 17"><path d="M8 2H2v13h13V9" fill="none" stroke="#b8914a" stroke-width="1.8"/><path d="M6 11l1-3 7-7 2 2-7 7z" fill="#b8914a"/></svg></span></div>
    <div class="row striped" style="top:713px"><span class="cell c-quote">001082</span><span class="cell c-customer">Milo Trevasset</span><span class="cell c-date">22 Jul 2017</span><span class="cell c-value">$3,100.00</span><span class="cell c-desc">New Apartment</span><span class="cell c-edit"><svg width="17" height="17" viewBox="0 0 17 17"><path d="M8 2H2v13h13V9" fill="none" stroke="#b8914a" stroke-width="1.8"/><path d="M6 11l1-3 7-7 2 2-7 7z" fill="#b8914a"/></svg></span></div>
    <div class="row" style="top:762px"><span class="cell c-quote">000728</span><span class="cell c-customer">Gideon Sallowby</span><span class="cell c-date">14 Jul 2016</span><span class="cell c-value">$4,200.00</span><span class="cell c-desc">New House</span><span class="cell c-edit"><svg width="17" height="17" viewBox="0 0 17 17"><path d="M8 2H2v13h13V9" fill="none" stroke="#b8914a" stroke-width="1.8"/><path d="M6 11l1-3 7-7 2 2-7 7z" fill="#b8914a"/></svg></span></div>
  </section>

  <div class="fab">
    <svg width="26" height="26" viewBox="0 0 26 26"><path d="M13 1v24M1 13h24" stroke="#fff" stroke-width="3"/></svg>
  </div>
</body>
</html>
```